Manuka honey wholesales and exports

We need business cards for our honey distribution company based in New Zealand. We supply shops locally and export Manuka honey around the world.
We deal with a very high quality and 100% natural product that can be used for medical, general health as well as food. We are looking business cards that show our honey products are of a high quality with a modern look.

Target Market(s)

Health and medical retailers and importers

Industry/Entity Type

Wholesale

Contact Information for Business Card

Tevin Apiary NZ Limited

www.tevinapiarynz.example

Derek Fawley

M +64 219036482

E tevinapiarynz@mailbox.example

PO Box 58-214
Kowhai Bay
East Shore
Auckland
New Zealand

Font styles to use
Serif

Requirements
Must have
• (Tevin Apiary NZ Limited) with some artwork on one side and all details on the other side.
Nice to have
• I have seen a very simple card with large yellow and black stripes on one side with a company name.. looked clean and simple so something similar or just let the creative beast inside you take over and we will see what you can come up with.

```html
<!DOCTYPE html>
<html lang="en">
<head>
<meta charset="utf-8">
<title>Tevin Apiary NZ Limited – Business Card</title>
<link rel="stylesheet" href="https://fonts.googleapis.com/css2?family=Tinos&display=swap">
<style>
  :root {
    --backdrop: #4d4d4d;
    --honey-yellow: #f4ea1a;
    --comb-tone: #e6dc12;
    --ink: #0d0d0d;
  }
  * { margin: 0; padding: 0; box-sizing: border-box; }
  html, body {
    width: 1200px;
    height: 900px;
    overflow: hidden;
  }
  body {
    position: relative;
    background: var(--backdrop);
  }
  .card {
    position: absolute;
    top: 113px;
    width: 390px;
    height: 667px;
    background: var(--honey-yellow);
    overflow: hidden;
  }
  .card--front { left: 168px; }
  .card--back {
    left: 647px;
    background: repeating-linear-gradient(
      to bottom,
      var(--honey-yellow) 0 18px,
      var(--ink) 18px 46px,
      var(--honey-yellow) 46px 55px
    );
  }
  .comb-area {
    position: absolute;
  }
  .comb-area--top { right: 0; top: 0; }
  .comb-area--bottom { left: 0; bottom: 0; }

  .contact {
    position: absolute;
    left: 0;
    right: 0;
    top: 260px;
    text-align: center;
    color: var(--ink);
    font-family: "Tinos", "Times New Roman", serif;
  }
  .contact__name {
    font-size: 34px;
    font-weight: 400;
    line-height: 40px;
    margin-bottom: 8px;
  }
  .contact__line {
    font-size: 16.5px;
    line-height: 20.5px;
  }
  .contact__address {
    margin-top: 11px;
  }

  .name-band {
    position: absolute;
    left: 0;
    right: 0;
    top: 274px;
    height: 119px;
    background: var(--honey-yellow);
    display: flex;
    flex-direction: column;
    align-items: center;
    justify-content: center;
    color: var(--ink);
    font-family: "Tinos", "Times New Roman", serif;
    font-weight: 400;
  }
  .name-band__name {
    font-size: 34px;
    line-height: 40px;
  }
  .name-band__suffix {
    font-size: 20px;
    line-height: 26px;
  }
</style>
</head>
<body>
  <section class="card card--front">
    <svg class="comb-area comb-area--top" width="260" height="224" viewBox="0 0 260 224" role="img" aria-label="Honeycomb pattern decoration">
      <polygon points="30,0 260,0 260,190 200,224 160,224 50,180 0,80" fill="var(--comb-tone)"/>
    </svg>

    <div class="contact">
      <h1 class="contact__name">Derek Fawley</h1>
      <p class="contact__line">M : +64 219036482</p>
      <p class="contact__line">E : tevinapiarynz@mailbox.example</p>
      <p class="contact__line">www.tevinapiarynz.example</p>
      <div class="contact__address">
        <p class="contact__line">PO Box 58-214, Kowhai Bay, East Shore</p>
        <p class="contact__line">Auckland, New Zealand</p>
      </div>
    </div>

    <svg class="comb-area comb-area--bottom" width="250" height="145" viewBox="0 0 250 145" role="img" aria-label="Honeycomb pattern decoration">
      <polygon points="0,30 60,0 110,30 165,50 250,110 250,145 0,145" fill="var(--comb-tone)"/>
    </svg>
  </section>

  <section class="card card--back">
    <div class="name-band">
      <p class="name-band__name">Tevin Apiary</p>
      <p class="name-band__suffix">NZ Limited</p>
    </div>
  </section>
</body>
</html>
```